CRPG is needing business cards, and stationary created.

Pixel Forge created a logo for our business, and now we are wanting business cards, and stationary. I have included two designs of the same logo. Please feel free to use them as you want. The name of the company is Cedar Ridge Property Group LLC, the address is 812 NE Willow Ln., Suite 9, the city & state is Bend, Oregon, zip code is 97815, Telephone number is 541-327-4489, Fax number is 541-327-6051, the name on the business card is Carl Whitby CMCA

Industry/Entity Type

Property Management

Contact Information for Business Card

The card needs to look professional. Upscale.

Requirements
Must have
• The colors we are using are on the logo that has been uploaded.

```html
<!DOCTYPE html>
<html lang="en">
<head>
<meta charset="utf-8">
<title>Cedar Ridge Property Group – Business Card</title>
<link rel="stylesheet" href="https://fonts.googleapis.com/css2?family=Saira:wght@700&family=Open+Sans:wght@400;600&display=swap">
<style>
  :root {
    --teal: #148a72;
    --slate: #3a4758;
    --ink: #2b2f36;
    --paper: #ffffff;
    --backdrop: #b4b4b4;
    --rule: #b9bec4;
  }
  * { box-sizing: border-box; margin: 0; padding: 0; }
  html, body { width: 1200px; height: 923px; overflow: hidden; }
  body {
    background: radial-gradient(ellipse at center, #c9c9c9 0%, var(--backdrop) 70%, #a3a3a3 100%);
    font-family: "Open Sans", sans-serif;
    color: var(--ink);
    position: relative;
  }
  .card {
    position: absolute;
    left: 250px;
    width: 700px;
    height: 400px;
    background: var(--paper);
    border-radius: 34px;
    overflow: hidden;
    box-shadow: 0 6px 18px rgba(0,0,0,0.22);
  }
  .card-front { top: 34px; }
  .card-back { top: 489px; }

  .lockup { position: absolute; text-align: center; }
  .lockup-mark { display: block; background: var(--slate); border-radius: 4px; }
  .brand-name {
    font-family: "Saira", sans-serif;
    font-weight: 700;
    color: var(--teal);
    line-height: 1;
    letter-spacing: 1px;
  }
  .brand-name .sub { display: block; }
  .tagline {
    font-family: "Open Sans", sans-serif;
    color: var(--slate);
    text-transform: uppercase;
    letter-spacing: 0.9em;
    white-space: nowrap;
  }

  /* front */
  .card-front .lockup { left: 0; right: 0; top: 62px; }
  .card-front .lockup-mark { width: 62px; height: 62px; margin: 0 auto 20px; }
  .card-front .brand-name { font-size: 68px; }
  .card-front .brand-name .sub { font-size: 21px; letter-spacing: 4px; margin-top: 8px; }
  .card-front .tagline { font-size: 12px; margin-top: 12px; }
  .website {
    position: absolute; left: 0; right: 0; top: 318px;
    text-align: center; font-size: 21px; letter-spacing: 4px; color: var(--ink);
  }

  /* back */
  .card-back .lockup { left: 88px; top: 40px; display: flex; align-items: center; gap: 22px; text-align: left; }
  .card-back .lockup-mark { width: 82px; height: 82px; }
  .card-back .brand-name { font-size: 56px; }
  .card-back .brand-name .sub { font-size: 16px; letter-spacing: 3px; margin-top: 8px; }
  .card-back .tagline { font-size: 10px; margin-top: 8px; letter-spacing: 0.8em; }

  .address {
    position: absolute; right: 392px; top: 168px;
    text-align: right; font-size: 18px; line-height: 1.3; font-style: normal;
  }
  .divider { position: absolute; left: 326px; top: 176px; width: 1px; height: 74px; background: var(--rule); }
  .contacts { position: absolute; left: 346px; top: 170px; list-style: none; font-size: 19px; line-height: 1.35; }
  .contacts li { display: flex; align-items: center; gap: 14px; }
  .contacts svg { width: 20px; height: 20px; fill: var(--slate); flex: none; }

  .band { position: absolute; left: 0; top: 0; width: 700px; height: 400px; }
  .holder-name {
    position: absolute; left: 120px; bottom: 12px;
    font-family: "Saira", sans-serif; font-weight: 700;
    font-size: 28px; line-height: 1.2; color: var(--paper); letter-spacing: 1px;
  }
</style>
</head>
<body>

<section class="card card-front">
  <div class="lockup">
    <span class="lockup-mark"></span>
    <div class="brand-name">CEDAR RIDGE<span class="sub">PROPERTY GROUP</span></div>
    <div class="tagline">Rooted in service</div>
  </div>
  <div class="website">www.cedarridgepg.com</div>
</section>

<section class="card card-back">
  <svg class="band" viewBox="0 0 700 400" aria-hidden="true">
    <path d="M0,236 C170,300 380,330 700,332 L700,334 C380,336 170,320 0,254 Z" fill="#148a72"/>
    <path d="M0,266 C170,325 380,344 700,342 L700,400 L0,400 Z" fill="#3a4758"/>
  </svg>

  <div class="lockup">
    <span class="lockup-mark"></span>
    <div>
      <div class="brand-name">CEDAR RIDGE<span class="sub">PROPERTY GROUP</span></div>
      <div class="tagline">Rooted in service</div>
    </div>
  </div>

  <address class="address">
    812 NE Willow Ln., Suite 9<br>
    the city &amp; state is Bend<br>
    Oregon, zip code is 97815
  </address>
  <span class="divider"></span>
  <ul class="contacts">
    <li>
      <svg viewBox="0 0 24 24"><path d="M6.6 10.8a15 15 0 0 0 6.6 6.6l2.2-2.2c.3-.3.7-.4 1-.2 1.1.4 2.3.6 3.6.6.6 0 1 .4 1 1V20c0 .6-.4 1-1 1A17 17 0 0 1 3 4c0-.6.4-1 1-1h3.5c.6 0 1 .4 1 1 0 1.3.2 2.5.6 3.6.1.3 0 .7-.2 1z"/></svg>
      541-327-4489
    </li>
    <li>
      <svg viewBox="0 0 24 24"><path d="M7 3h8l2 2v4H7z M3 10h18v9H3z M7 15h10v6H7z"/></svg>
      541-327-6051
    </li>
    <li>
      <svg viewBox="0 0 24 24"><path d="M2 5h20v14H2z M3.5 6.5 12 13l8.5-6.5" fill="none" stroke="#3a4758" stroke-width="2"/></svg>
      info@cedarridgepg.com
    </li>
  </ul>

  <div class="holder-name">CARL WHITBY, CMCA</div>
</section>

</body>
</html>
```